Quillet Studios business card

Front of card should be logo and back of card should be communication info.
Please note: reverse the logo color. Card should be black and everything else white.

Industry/Entity Type

Custom home design/construction

Contact Information for Business Card

Quillet Studios, LLC 555-382-0146 quilletstudios@mailbox-example.com

Requirements
Must have
• Square card, Logo on front, communication info on back and perhaps a mini version of the logo on back also. Black card/white lettering. Double sides square card.
Nice to have
• I want to keep it simple. Our product (custom homes) speak for themselves.

```html
<!DOCTYPE html>
<html lang="en">
<head>
<meta charset="utf-8">
<title>Quillet Studios — Square Business Card</title>
<link rel="stylesheet" href="https://fonts.googleapis.com/css2?family=Montserrat:wght@500;600&family=Poppins:wght@300;400;500;600&display=swap">
<style>
  :root {
    --backdrop: #dcdcdc;
    --card: #1a1a1a;
    --ink: #ffffff;
    --ink-soft: #e6e6e6;
    --rule: #8a8a8a;
    --art-tone: #3b3b3b;
    --pattern-dark: #141414;
    --pattern-mid: #2e2e2e;
  }
  * { margin: 0; padding: 0; box-sizing: border-box; }
  html, body {
    width: 1200px; height: 900px; overflow: hidden;
    background: var(--backdrop);
  }
  .canvas { position: relative; width: 1200px; height: 900px; }
  .card {
    position: absolute; top: 256px;
    width: 398px; height: 399px;
    background: var(--card);
    color: var(--ink);
    overflow: hidden;
  }
  .card--front { left: 205px; }
  .card--back { left: 653px; }

  .house-art {
    position: absolute; left: 130px; top: 29px;
    width: 140px; height: 102px;
    background: linear-gradient(180deg, var(--art-tone), #2a2a2a);
  }
  .brand {
    position: absolute; left: 0; right: 0; top: 134px;
    text-align: center;
  }
  .brand__name {
    font-family: "Montserrat", sans-serif;
    font-weight: 600; font-size: 23px; letter-spacing: 0.5px;
    line-height: 1.1;
  }
  .brand__tagline {
    font-family: "Montserrat", sans-serif;
    font-weight: 500; font-size: 14.5px; letter-spacing: 1.6px;
    color: var(--ink-soft); line-height: 1.2; margin-top: 2px;
  }
  .contact {
    position: absolute; left: 0; right: 0; top: 246px;
    text-align: center;
    font-family: "Poppins", sans-serif;
  }
  .contact__name { font-weight: 600; font-size: 20px; letter-spacing: 0.6px; line-height: 1.2; }
  .contact__role { font-weight: 400; font-size: 14.5px; letter-spacing: 0.3px; margin-top: 2px; }
  .contact__rule {
    width: 108px; height: 1px; background: var(--rule);
    margin: 10px auto 12px;
  }
  .contact__phone { font-weight: 300; font-size: 18px; letter-spacing: 0.5px; }
  .contact__email { font-weight: 400; font-size: 12.5px; letter-spacing: 0.3px; margin-top: 8px; }

  .pattern-field {
    position: absolute; inset: 0;
    background: linear-gradient(150deg, var(--pattern-dark) 0%, var(--pattern-mid) 45%, var(--pattern-dark) 70%, var(--pattern-mid) 100%);
  }
  .mini-brand {
    position: absolute; left: 78px; top: 228px;
    font-family: "Montserrat", sans-serif;
    color: var(--ink);
  }
  .mini-brand__name { font-weight: 600; font-size: 18px; letter-spacing: 0.5px; line-height: 1.1; }
  .mini-brand__tagline { font-weight: 500; font-size: 11.5px; letter-spacing: 1.3px; margin-top: 1px; }
</style>
</head>
<body>
<main class="canvas">
  <section class="card card--front">
    <div class="house-art" role="img" aria-label="Line illustration of a two-storey custom home"></div>
    <div class="brand">
      <p class="brand__name">QUILLET STUDIOS</p>
      <p class="brand__tagline">CUSTOM HOME BUILDERS</p>
    </div>
    <div class="contact">
      <p class="contact__name">MARCUS DELANEY</p>
      <p class="contact__role">MANAGING DIRECTOR</p>
      <div class="contact__rule"></div>
      <p class="contact__phone">555-382-0146</p>
      <p class="contact__email">QUILLETSTUDIOS@MAILBOX-EXAMPLE.COM</p>
    </div>
  </section>

  <section class="card card--back">
    <div class="pattern-field" role="img" aria-label="Faint repeating diagonal brand-name pattern in glossy black"></div>
    <div class="mini-brand">
      <p class="mini-brand__name">QUILLET STUDIOS</p>
      <p class="mini-brand__tagline">CUSTOM HOME BUILDERS</p>
    </div>
  </section>
</main>
</body>
</html>
```